Dorvelan Swimming & Athletics Center

We need Business Card for a Athletics center
The logo frome the Uploaded Files ( b card fimal)
Οn one side of card we need the logo of company the Contact and the website:
1. Address:(Limassol, Cyprus 12-14 Stavrinelou str,Ano Trimeni,P.C. 4832)

2.Phone number: (+357) 25-704263

3. Mail: info@dorvelanfit.example

3. Website: www.dorvelanfit.example

Οn the other side of the card we need to write the sport of the company:

1. Artistic Gymnastics
2. Swimming
3. Gym - Fitness
4. Programs
5. Dancing
5.Tennis

From the Uploaded Files you can get the logo.In a logo is behind the black color which can be removed from logo.

Υou can use that color you want.
.
Updates

Industry/Entity Type

Business

Font styles to use
Decorative

Colors
0555a3
ffcf3e
3176b5
0692cd
add136
f04a50
000000
cfcfcf
9d9d9d

Requirements
Should not have
• photos with faces
• photo fro the Website:www.dorvelanfit.example

```html
<!DOCTYPE html>
<html lang="en">
<head>
<meta charset="utf-8">
<title>Dorvelan Swimming &amp; Athletics Center – Business Card</title>
<link rel="stylesheet" href="https://fonts.googleapis.com/css2?family=Oswald:wght@300;400;600&display=swap">
<style>
  :root {
    --navy: #0555a3;
    --gold: #ffcf3e;
    --mid-blue: #3176b5;
    --sky: #0692cd;
    --lime: #add136;
    --red: #f04a50;
    --black: #050303;
    --light-grey: #cfcfcf;
    --grey: #9d9d9d;
    --stage: #c4c4c4;
    --white: #ffffff;
  }
  * { margin: 0; padding: 0; box-sizing: border-box; }
  html, body { width: 1200px; height: 1200px; overflow: hidden; }
  body {
    background: var(--stage);
    font-family: "Oswald", sans-serif;
    position: relative;
  }
  .card {
    position: absolute;
    left: 170px;
    width: 860px;
    height: 518px;
    overflow: hidden;
  }
  /* Front side */
  .card-front { top: 58px; background: var(--black); color: var(--white); }
  .brand-name {
    position: absolute;
    top: 158px;
    left: 98px;
    width: 540px;
    font-weight: 600;
    font-size: 88px;
    line-height: 1;
    letter-spacing: 20px;
    white-space: nowrap;
    color: var(--gold);
  }
  .brand-mark {
    position: absolute;
    top: 148px;
    left: 658px;
    width: 120px;
    height: 120px;
    border-radius: 50%;
    border: 4px solid var(--gold);
  }
  .website {
    position: absolute;
    top: 295px;
    width: 100%;
    text-align: center;
    font-weight: 300;
    font-size: 23px;
    line-height: 34px;
    letter-spacing: 1.5px;
  }
  .divider {
    position: absolute;
    top: 371px;
    left: 158px;
    width: 544px;
    height: 1px;
    background: var(--light-grey);
  }
  .contacts {
    position: absolute;
    top: 384px;
    width: 100%;
    text-align: center;
    font-weight: 300;
    font-size: 23px;
    line-height: 37px;
  }
  .contacts .label { color: var(--gold); }
  .color-strip {
    position: absolute;
    left: 0; right: 0; bottom: 0;
    height: 6px;
    display: flex;
  }
  .color-strip span, .side-bar span { flex: 1; }
  .c1 { background: var(--lime); }
  .c2 { background: var(--sky); }
  .c3 { background: var(--mid-blue); }
  .c4 { background: var(--gold); }
  .c5 { background: var(--grey); }
  .c6 { background: var(--red); }

  /* Back side */
  .card-back { top: 638px; background: var(--white); }
  .side-bar {
    position: absolute;
    top: 0; bottom: 0;
    width: 10px;
    display: flex;
    flex-direction: column;
  }
  .side-bar.left { left: 0; }
  .side-bar.right { right: 0; }
  .back-ring {
    position: absolute;
    left: 200px;
    top: 38px;
    width: 440px;
    height: 440px;
    border-radius: 50%;
    border: 14px solid #f1f1f1;
  }
  .sports { position: absolute; left: 0; top: 0; }
  .sport-label {
    font-family: "Oswald", sans-serif;
    font-weight: 300;
    font-size: 25px;
    fill: var(--white);
  }
</style>
</head>
<body>

<section class="card card-front">
  <span class="brand-name">DORVELAN</span>
  <span class="brand-mark"></span>
  <p class="website">www.dorvelanfit.example</p>
  <div class="divider"></div>
  <div class="contacts">
    <p><span class="label">A:</span> Limassol, Cyprus 12-14 Stavrinelou str, Ano Trimeni, P.C. 4832</p>
    <p><span class="label">P:</span> (+357) 25-704263</p>
    <p><span class="label">M:</span> info@dorvelanfit.example</p>
  </div>
  <div class="color-strip">
    <span class="c1"></span><span class="c2"></span><span class="c3"></span>
    <span class="c4"></span><span class="c5"></span><span class="c6"></span>
  </div>
</section>

<section class="card card-back">
  <div class="back-ring"></div>
  <div class="side-bar left">
    <span class="c1"></span><span class="c2"></span><span class="c3"></span>
    <span class="c4"></span><span class="c5"></span><span class="c6"></span>
  </div>
  <div class="side-bar right">
    <span class="c1"></span><span class="c2"></span><span class="c3"></span>
    <span class="c4"></span><span class="c5"></span><span class="c6"></span>
  </div>
  <svg class="sports" width="860" height="518" viewBox="0 0 860 518" aria-label="Sports offered">
    <defs>
      <g id="sport-tab">
        <line x1="70" y1="0" x2="788" y2="0" stroke="#050303" stroke-width="2.5"/>
        <polygon points="252,0 278,-32 622,-32 592,0" fill="#050303"/>
        <line x1="262" y1="-3" x2="284" y2="-30" stroke="#fff" stroke-width="2"/>
        <line x1="592" y1="-3" x2="614" y2="-30" stroke="#fff" stroke-width="2"/>
      </g>
    </defs>
    <g transform="translate(0,114)"><use href="#sport-tab"/><text class="sport-label" x="439" y="-7" text-anchor="middle">Artistic Gymnastics</text></g>
    <g transform="translate(0,181)"><use href="#sport-tab"/><text class="sport-label" x="439" y="-7" text-anchor="middle">Swimming</text></g>
    <g transform="translate(0,248)"><use href="#sport-tab"/><text class="sport-label" x="439" y="-7" text-anchor="middle">Gym - Fitness</text></g>
    <g transform="translate(0,316)"><use href="#sport-tab"/><text class="sport-label" x="439" y="-7" text-anchor="middle">Programs</text></g>
    <g transform="translate(0,383)"><use href="#sport-tab"/><text class="sport-label" x="439" y="-7" text-anchor="middle">Dancing</text></g>
    <g transform="translate(0,450)"><use href="#sport-tab"/><text class="sport-label" x="439" y="-7" text-anchor="middle">Tennis</text></g>
  </svg>
</section>

</body>
</html>
```